Marla Fenwick Book Cover

- 6x9 book cover.
- Book title: Planting the dry-ground seeds - a gardener's patient season from frost to harvest
- Back cover will show the 3 testimonials along with their pictures ( we only have two atm, so please just leave a space for a 3rd ). Back cover will also include "about the author"
- Front cover to feature author's picture and background should have nature view ( outside window )
- Author's text: ( The language about me )
This is one woman’s story about her journey from the depths of despair to happiness and financial success. She stopped chasing the Dry-Ground Seeds. Marla shares the steps she then took to change her life.
Listed in Pinecrest Honors Roll, Harwick Register Series and more Marla Fenwick provides hands on, real life advice to help you make remarkable changes in your life.

```html
<!DOCTYPE html>
<html lang="en">
<head>
<meta charset="utf-8">
<title>Marla Fenwick Book Cover</title>
<link href="https://fonts.googleapis.com/css2?family=Dancing+Script:wght@700&family=Playfair+Display&family=Montserrat:wght@300&family=Oswald:wght@300;400;500&display=swap" rel="stylesheet">
<style>
  :root {
    --stage: #ececec;
    --ink: #141414;
    --white: #ffffff;
    --accent-yellow: #f1f233;
    --leaf-light: #c9d6a6;
    --leaf-mid: #6f8f3e;
    --leaf-deep: #34481c;
    --leaf-dark: #1f2b10;
    --sky: #eef1ea;
    --portrait: #b9b2a8;
    --portrait-dark: #6b5a4e;
  }
  * { margin: 0; padding: 0; box-sizing: border-box; }
  html, body { width: 1200px; height: 1041px; overflow: hidden; }
  body { background: var(--stage); position: relative; font-family: "Oswald", sans-serif; }

  .cover { position: absolute; top: 160px; width: 480px; height: 720px; overflow: hidden; }
  .front-cover { left: 90px; }
  .back-cover { left: 610px; }
  .spine { position: absolute; top: 160px; left: 1090px; width: 42px; height: 720px;
    background: linear-gradient(180deg, var(--leaf-deep), var(--leaf-dark));
    display: flex; align-items: center; justify-content: center; }
  .spine-title { writing-mode: vertical-rl; transform: rotate(180deg); color: var(--white);
    font: 500 19px "Oswald", sans-serif; letter-spacing: 3px; text-transform: uppercase; white-space: nowrap; }

  .scene-photo { position: absolute; inset: 0; }
  .front-cover .scene-photo {
    background:
      linear-gradient(180deg, rgba(0,0,0,0) 70%, rgba(20,28,10,0.85) 100%),
      radial-gradient(ellipse at 75% 45%, #a9b95a 0%, rgba(169,185,90,0) 45%),
      linear-gradient(180deg, var(--sky) 0%, var(--leaf-light) 22%, var(--leaf-mid) 55%, var(--leaf-deep) 85%);
  }
  .back-cover .scene-photo {
    background:
      radial-gradient(ellipse at 70% 30%, #6f8a35 0%, rgba(111,138,53,0) 55%),
      linear-gradient(180deg, var(--leaf-deep) 0%, #3f5520 50%, var(--leaf-dark) 85%, #4f6a24 100%);
  }

  .title-script { position: absolute; top: 22px; left: 56px; font: 700 82px "Dancing Script", cursive; color: var(--ink); line-height: 1; }
  .title-serif { position: absolute; top: 120px; left: 80px; font: 400 34px "Playfair Display", serif; color: var(--white); line-height: 1; white-space: nowrap; }
  .subtitle { position: absolute; top: 176px; left: 48px; font: 300 9.5px "Montserrat", sans-serif; letter-spacing: 1.2px; color: #333; text-transform: uppercase; white-space: nowrap; }

  .author-portrait { position: absolute; top: 590px; left: 40px; width: 88px; height: 100px; border-radius: 50%;
    background: radial-gradient(circle at 50% 40%, var(--portrait) 0%, var(--portrait-dark) 100%);
    border: 2px solid rgba(255,255,255,0.4); }
  .author-blurb { position: absolute; top: 600px; left: 138px; width: 320px; font: 400 10.5px/1.7 "Oswald", sans-serif; color: var(--white); }

  .section-heading { position: absolute; font: 500 30px/1.2 "Oswald", sans-serif; color: var(--accent-yellow); letter-spacing: 2px; text-transform: uppercase; }
  .about-heading { top: 40px; left: 70px; }
  .about-text { position: absolute; top: 96px; left: 26px; width: 380px; font: 300 10.5px/1.75 "Oswald", sans-serif; color: var(--white); }
  .testimonial-heading { top: 222px; left: 106px; }

  .testimonial { position: absolute; left: 0; width: 480px; }
  .testimonial-one { top: 290px; }
  .testimonial-two { top: 420px; }
  .testimonial-three { top: 590px; }
  .testimonial-portrait { position: absolute; top: 0; left: 0; width: 86px; height: 86px; border-radius: 50%;
    background: radial-gradient(circle at 50% 40%, #d9d9d9 0%, #8a7566 100%); }
  .testimonial-quote { position: absolute; top: 6px; left: 108px; width: 270px; font: 300 10.5px/1.7 "Oswald", sans-serif; color: var(--white); }
  .testimonial-credit { display: block; margin-top: 6px; font-size: 12px; line-height: 1.4; color: var(--accent-yellow); font-weight: 400; font-style: normal; }
</style>
</head>
<body>

<section class="cover front-cover">
  <div class="scene-photo" role="img" aria-label="Photo of a woman leaping from a tree stump into a green valley with trees"></div>
  <h1 class="title-script">Planting</h1>
  <p class="title-serif">the dry-ground seeds</p>
  <p class="subtitle">A gardener's patient season from frost to harvest</p>
  <div class="author-portrait" role="img" aria-label="Portrait photo of author Marla Fenwick"></div>
  <p class="author-blurb">This is one woman's story about her journey from the depths of despair to happiness and financial success. She stopped chasing the Dry-Ground Seeds. Marla shares the steps she then took to change her life. Listed in Pinecrest Honors Roll, Harwick Register Series and more Marla Fenwick provides hands on, real life advice to help you make remarkable changes in your life.</p>
</section>

<section class="cover back-cover">
  <div class="scene-photo" role="img" aria-label="Soft-focus photo of green trees and grass"></div>
  <h2 class="section-heading about-heading">About the Author</h2>
  <p class="about-text">Lorem ipsum dolor sit amet, consectetur adipiscing elit, sed do eiusmod tempor incididunt ut labore et dolore magna aliqua. Ut enim ad minim veniam, quis nostrud exercitation ullamco laboris nisi ut aliquip ex ea commodo consequat. Duis aute irure dolor in reprehenderit in voluptate velit esse cillum dolore eu fugiat nulla pariatur. Excepteur sint occaecat cupidatat non proident, sunt in culpa qui officia deserunt mollit anim id est laborum</p>

  <h2 class="section-heading testimonial-heading">Testimonials</h2>

  <figure class="testimonial testimonial-one">
    <div class="testimonial-portrait" role="img" aria-label="Portrait photo of Joan Whitley"></div>
    <blockquote class="testimonial-quote">“As a clarity, leadership &amp; communication strategist, I found Marla's advice to be down to earth, providing a no-nonsense foundation to begin making the life changes women want.”
      <cite class="testimonial-credit">Joan Whitley, Author of the Quiet Ledger</cite>
    </blockquote>
  </figure>

  <figure class="testimonial testimonial-two">
    <div class="testimonial-portrait" role="img" aria-label="Portrait photo of Renata Okafor"></div>
    <blockquote class="testimonial-quote">As our world gets increasingly more stressful, the complexities of trying to develop true balance in our lives, work, and relationships adds more stress. In her book, Marla Fenwick offers sound advice on how to create and maintain a healthy lifestyle. This book is a must have!
      <cite class="testimonial-credit">Renata Okafor: Harbor Flood Survivor, Lakeshore Ledger Best-Selling Author and Founder of The Common Table Project</cite>
    </blockquote>
  </figure>

  <figure class="testimonial testimonial-three">
    <div class="testimonial-portrait" role="img" aria-label="Portrait photo of third testimonial author"></div>
    <blockquote class="testimonial-quote">“As a clarity, leadership &amp; communication strategist, I found Marla's advice to be down to earth, providing a no-nonsense foundation to begin making the life changes women want.”
      <cite class="testimonial-credit">Joan Whitley, Author of the Quiet Ledger</cite>
    </blockquote>
  </figure>
</section>

<aside class="spine">
  <span class="spine-title">Planting the dry-ground seeds</span>
</aside>

</body>
</html>
```